Consulting Company needs business card design

We need a business card design for a new consulting and business solutions company based in Bermuda called Corvale Partners Limited. Looking for a double sided business card with one side only including the company logo thats attached and the other including contact information. Logo contains blue and turquoise colors and is fine to be on both sides of the card.
Contact Information for Business Card
Corvale Partners Limited
P.O. Box HM318
Devonshire DV BX
Bermuda
Name: Marcus Pellegrin
Position: Director
Telephone: 1 441 733 4906
Email: mpellegrin@corvale.example
Website: www.corvale.example

```html
<!DOCTYPE html>
<html lang="en">
<head>
<meta charset="utf-8">
<title>Corvale Partners Limited – Business Card</title>
<link href="https://fonts.googleapis.com/css2?family=Montserrat:wght@400;600;700&display=swap" rel="stylesheet">
<style>
  :root {
    --page: #ffffff;
    --card: #ffffff;
    --card-edge: #a9a9a9;
    --ink: #1b1b1b;
    --ink-soft: #3a3a3a;
    --brand-blue: #4cc9f0;
    --brand-turquoise: #3ef2b6;
    --divider: #9a9a9a;
  }
  * { box-sizing: border-box; margin: 0; padding: 0; }
  html, body {
    width: 1200px; height: 336px; overflow: hidden;
    background: var(--page);
    font-family: "Montserrat", Arial, sans-serif;
  }
  .sheet { position: relative; width: 1200px; height: 336px; }
  .card {
    position: absolute; top: 3px; height: 330px;
    background: var(--card);
    border: 1px solid var(--card-edge);
  }
  .card--front { left: 3px; width: 581px; }
  .card--back { left: 615px; width: 582px; }

  .wordmark {
    position: absolute;
    display: flex; align-items: center;
    color: var(--brand-blue);
    font-weight: 600;
  }
  .wordmark__dot {
    flex: none; border-radius: 50%;
    background: var(--brand-blue);
  }
  .wordmark__text { display: flex; flex-direction: column; line-height: 1; }
  .wordmark__name { letter-spacing: 0.02em; }
  .wordmark__sub { letter-spacing: 0.2em; margin-top: 8px; }

  .card--front .wordmark { left: 85px; top: 108px; gap: 18px; }
  .card--front .wordmark__dot { width: 96px; height: 96px; }
  .card--front .wordmark__name { font-size: 56px; }
  .card--front .wordmark__sub { font-size: 17px; }

  .card--back .wordmark { left: 316px; top: 140px; gap: 10px; }
  .card--back .wordmark__dot { width: 46px; height: 46px; }
  .card--back .wordmark__name { font-size: 27px; }
  .card--back .wordmark__sub { font-size: 8.5px; margin-top: 4px; }

  .contact { position: absolute; left: 27px; top: 68px; color: var(--ink); }
  .contact__name { font-size: 17px; font-weight: 700; letter-spacing: 0.03em; }
  .contact__role { font-size: 15px; font-weight: 400; margin-top: 4px; color: var(--ink-soft); letter-spacing: 0.02em; }
  .contact__lines { list-style: none; margin-top: 28px; }
  .contact__lines li { font-size: 12.5px; font-weight: 700; letter-spacing: 0.08em; line-height: 20.5px; }
  .contact__address { font-style: normal; margin-top: 23px; font-size: 12.5px; line-height: 19px; color: var(--ink-soft); }

  .divider {
    position: absolute; left: 264px; top: 18px; width: 3px; height: 296px;
    background: linear-gradient(to bottom, transparent, var(--divider) 30%, var(--divider) 70%, transparent);
    clip-path: polygon(50% 0, 100% 50%, 50% 100%, 0 50%);
  }
</style>
</head>
<body>
<div class="sheet">
  <section class="card card--front" aria-label="Card front">
    <div class="wordmark">
      <span class="wordmark__dot"></span>
      <span class="wordmark__text">
        <span class="wordmark__name">CORVALE</span>
        <span class="wordmark__sub">PARTNERS LIMITED</span>
      </span>
    </div>
  </section>

  <section class="card card--back" aria-label="Card back">
    <div class="contact">
      <p class="contact__name">Marcus Pellegrin</p>
      <p class="contact__role">Director</p>
      <ul class="contact__lines">
        <li>t: 1 441 733 4906</li>
        <li>e: mpellegrin@corvale.example</li>
        <li>w: www.corvale.example</li>
      </ul>
      <address class="contact__address">
        Corvale Partners Limited<br>
        P.O. Box HM318<br>
        Devonshire DV BX<br>
        Bermuda
      </address>
    </div>
    <div class="divider"></div>
    <div class="wordmark">
      <span class="wordmark__dot"></span>
      <span class="wordmark__text">
        <span class="wordmark__name">CORVALE</span>
        <span class="wordmark__sub">PARTNERS LIMITED</span>
      </span>
    </div>
  </section>
</div>
</body>
</html>
```